Etiketten für Bio Seifen
Zielgruppe
Wir stellen hochwertig 'handgemachte' Bio-Seifen her. Die Zielgruppe ist von 3-99 Jahren und zusätzlich haben wir auch noch Seife für Hunde.
Der Firmenname ist 'Kestrima'
Aufgabenstellung
Das Etikett soll Bezug auf Natur, Bio, Nachhaltigkeit nehmen. Wir stellen uns 'weiche' Aquarellfarben vor...Seife: Lavendel, Calendular, 7 Kräuter etc.
Das Etikett soll auf eine Beutelschachtel. Die Schachtel hat eine Anmaße: Breite 55mm; Höhe 120mm; Tiefe 30mm
Das Etikett soll im vorderen- und hinteren Bereich zusammenhängend geklebt werden.
Das Etikett soll eine Abmaße von: Breite 51mm; Höhe 114mm haben (Vorderseite) Rückseite gleich.
Wir möchten die Produkte auch gerne nummerieren, d.h. jede Seife hat eine Nummer die nicht zu groß dargestellt werden soll aber trotzdem gut leserlich.
Wir haben noch ein paar Bilder hochgeladen wie wir uns das ungefähr vorstellen.

```html
<!DOCTYPE html>
<html lang="de">
<head>
<meta charset="utf-8">
<title>Kestrima – Bio Seife Lavendel Nr. 1</title>
<link rel="stylesheet" href="https://fonts.googleapis.com/css2?family=Jost:wght@300;400&family=Cinzel:wght@400;500&family=Mrs+Saint+Delafield&display=swap">
<style>
  :root {
    --paper: #ffffff;
    --wash-top: #8b80c6;
    --wash-mid: #7a86c8;
    --wash-low: #7f85c6;
    --wash-bottom: #9a7bc0;
    --ink: #3b2587;
    --panel: rgba(98, 72, 168, 0.55);
    --light: #f4f1ff;
  }
  * { margin: 0; padding: 0; box-sizing: border-box; }
  html, body {
    width: 1200px;
    height: 2582px;
    overflow: hidden;
    background: var(--paper);
  }
  .canvas {
    position: relative;
    width: 1200px;
    height: 2582px;
  }
  .label {
    position: absolute;
    left: 98px;
    top: 214px;
    width: 963px;
    height: 2154px;
    overflow: hidden;
  }
  .watercolor-leaves {
    position: absolute;
    inset: 0;
    background:
      radial-gradient(ellipse at 30% 20%, rgba(170, 160, 220, 0.35), transparent 55%),
      radial-gradient(ellipse at 80% 90%, rgba(170, 120, 200, 0.45), transparent 50%),
      linear-gradient(180deg, var(--wash-top) 0%, var(--wash-mid) 40%, var(--wash-low) 75%, var(--wash-bottom) 100%);
  }
  .title-frame {
    position: absolute;
    left: 46px;
    top: 696px;
    width: 882px;
    height: 618px;
    border: 4px solid var(--ink);
  }
  .title-panel {
    position: absolute;
    left: 18px;
    top: 16px;
    right: 18px;
    bottom: 16px;
    background: var(--panel);
  }
  .title-block {
    position: absolute;
    left: 0;
    right: 0;
    top: 0;
    text-align: center;
  }
  .brand {
    position: absolute;
    left: 0; right: 0;
    top: 797px;
    font-family: 'Jost', sans-serif;
    font-weight: 300;
    font-size: 86px;
    letter-spacing: 6px;
    color: var(--light);
    text-align: center;
    line-height: 1;
  }
  .category {
    position: absolute;
    left: 0; right: 0;
    top: 1110px;
    font-family: 'Jost', sans-serif;
    font-weight: 400;
    font-size: 34px;
    letter-spacing: 1px;
    color: var(--ink);
    text-align: center;
    line-height: 1;
  }
  .handmade {
    position: absolute;
    left: 0; right: 0;
    top: 1168px;
    font-family: 'Mrs Saint Delafield', cursive;
    font-size: 58px;
    color: rgba(240, 236, 255, 0.75);
    text-align: center;
    line-height: 1;
    letter-spacing: 2px;
  }
  .variety {
    position: absolute;
    left: 0; right: 0;
    top: 1232px;
    font-family: 'Cinzel', serif;
    font-weight: 500;
    font-size: 100px;
    letter-spacing: 2px;
    color: var(--ink);
    text-align: center;
    line-height: 1;
  }
  .number {
    position: absolute;
    left: 0; right: 0;
    top: 1352px;
    font-family: 'Cinzel', serif;
    font-weight: 500;
    font-size: 42px;
    color: var(--light);
    text-align: center;
    line-height: 1;
  }
</style>
</head>
<body>
<div class="canvas">
  <section class="label">
    <div class="watercolor-leaves" role="img" aria-label="Aquarellhintergrund in Lavendeltönen mit fein gezeichneten Blattranken"></div>
    <div class="title-frame">
      <div class="title-panel"></div>
    </div>
  </section>
  <div class="title-block">
    <h1 class="brand">KESTRIMA</h1>
    <p class="category">BIO SEIFE</p>
    <p class="handmade">Handgemachte</p>
    <h2 class="variety">Lavendel</h2>
    <p class="number">Nr. 1</p>
  </div>
</div>
</body>
</html>
```